Affiliate website design and wireframe

We need a design of an affiliate website for an application we purchased, it is important that you build the website pages according to the developer of the applications specifications (please see attached documents) the developer of the application will configure the pages and add them to the site. Please take special note of his comments below.

We all so need you to create a wire frame so the developer can test everything (http://quartz.lomeriva.vn/)

It will be the homepage and about 16 inner pages (please see attached files)
Here is our website http://maplecourtlink.com/affiliate/affiliates/index.php

The version of the software we purchased is the Quill Partner Grid version

Comments from the developers

1. I will need the source files of the design (photoshop .psd files and font files if custom fonts are used), since the implementation is closely bound to component sizes (like border width, margin width etc.) and colors. If you own a corporate design manual, it's crucial to send it as well. Also, please, make sure if you use custom fonts, that these allow legal website integration (like zorvix web fonts).

2. Any and every content is controlled via templates. All editing/adding/removing etc. is done here. The template files are essentially html/php documents, they use a template engine called brisko (http://www.brisko.net/) which has it's own language similar to php.

3. .psd files are ideal, because we deal with the specifics of QPS/QPG implementation on a daily basis. Any html/css developed in advance may prove to be a poor choice. You may choose to let an in-house developer do the job, but experience wise this is more costly, since he will not be accustomed to the template/functionality systems of QPS/QPG.

4. I will need the source files of the design (photoshop .psd files and font files if custom fonts are used), since the implementation is closely bound to component sizes (like border width, margin width etc.) and colors. If you own a corporate design manual, it's crucial to send it as well. Also, please, make sure if you use custom fonts, that these allow legal website integration (like zorvix web fonts).

Regards,

Tomas Vereck

We prefer illustrations more than pictures of real people.

This is the home page, it is asking for Merchant and Affiliate sign up, not just affiliate.

http://maplecourtlink.com/affiliate/index.php

Please note the home page features both Merchant and Affiliate sign up

We are looking for illustration design not just stock images

Please remember the search menu that searches for the available programs, see the example we gave you, look at the search menu at the top of the page http://www.tradolink.com/

We are reviewing everything, no need to send more designs

Target Market(s)

Natural Products Manufacturers
Natural products Sales reps
Natural Products Bloggers
Social Marketing

Industry/Entity Type

Software

Requirements
Must have
• 1. All links on pages should go to the appropriate pages.
2. Colors can be based on our logo design (look at the attachments)
3. Here is our website http://maplecourtlink.com/affiliate/affiliates/index.php
4. We have attached a drawing of how we think the homepage concept should follow.
5. Main concept of design, is trying to show our sales people (Affiliates) are doing multiple things to advertise and sell the merchants products.(see logo)
6. Need to be able to edit all text and images.
7. Our target audience is Natural product sales people (Advertisers, bloggers, ext) and natural product manufacturers.
8. You can speak to the company who made the application, through live chat, on there website http://www.quillpartnergrid.com/
Nice to have
• See Attached Documents.
site should take up whole website pages
Look For fun Illustrated Website, one of the better ones we have seen is http://www.tradolink.com/index.cfm
Should not have
• Please look very carefully at developers comment above.

```html
<!DOCTYPE html>
<html lang="en">
<head>
<meta charset="utf-8">
<title>How Does It Work – MapleCourt Affiliate</title>
<link rel="stylesheet" href="https://fonts.googleapis.com/css2?family=Open+Sans:wght@300;400;600;700&display=swap">
<style>
  :root {
    --navy: #1f3f6e;
    --navy-line: #27477a;
    --band: #2b5283;
    --band-dark: #234673;
    --green: #7dc242;
    --text: #5d6673;
    --muted: #9aa2ad;
    --white: #ffffff;
    --page: #ffffff;
  }
  * { box-sizing: border-box; margin: 0; padding: 0; }
  html, body { width: 1200px; height: 727px; overflow: hidden; background: var(--page); }
  body { font-family: "Open Sans", Arial, sans-serif; color: var(--text); position: relative; }

  .how-it-works { position: absolute; left: 0; top: 0; width: 1200px; height: 470px; background: var(--white); }
  .section-title {
    position: absolute; top: 34px; left: 0; width: 100%; text-align: center;
    font-size: 22px; font-weight: 600; color: var(--navy); letter-spacing: .5px;
  }
  .section-intro {
    position: absolute; top: 72px; left: 330px; width: 540px; text-align: center;
    font-size: 12px; line-height: 1.6; font-weight: 300;
  }
  .section-intro a { color: var(--navy); text-decoration: underline; }

  .process-diagram { position: absolute; left: 0; top: 0; }

  .hub-name {
    position: absolute; left: 540px; top: 262px; width: 120px; text-align: center;
    font-size: 15px; font-weight: 600; color: var(--navy);
  }

  .step { position: absolute; width: 210px; font-size: 11px; line-height: 1.5; font-weight: 300; }
  .step-number { display: block; font-size: 12px; font-weight: 400; color: var(--navy); margin-bottom: 4px; }
  .step--left { text-align: right; }
  .step-1 { left: 810px; top: 202px; }
  .step-2 { left: 810px; top: 318px; }
  .step-3 { left: 676px; top: 378px; }
  .step-4 { left: 210px; top: 262px; }
  .step-5 { left: 210px; top: 176px; }
  .step-6 { left: 676px; top: 138px; width: 190px; }

  .tagline {
    position: absolute; top: 430px; left: 0; width: 100%; text-align: center;
    font-size: 13px; font-weight: 600; color: var(--navy); letter-spacing: .3px;
  }

  .join-band {
    position: absolute; left: 0; top: 470px; width: 1200px; height: 257px;
    background: linear-gradient(180deg, var(--band) 0%, var(--band-dark) 100%);
    border-top: 3px solid var(--green);
  }
  .join-copy {
    position: absolute; left: 70px; top: 86px; width: 560px;
    font-size: 15px; line-height: 1.6; color: var(--white); font-weight: 400;
  }
  .join-arrow { position: absolute; left: 720px; top: 96px; }
  .join-button {
    position: absolute; left: 860px; top: 88px; width: 160px; height: 50px;
    border: 2px solid rgba(255,255,255,.85); color: var(--white);
    font-size: 15px; font-weight: 600; letter-spacing: 1px;
    display: flex; align-items: center; justify-content: center; text-decoration: none;
  }
</style>
</head>
<body>
  <section class="how-it-works">
    <h2 class="section-title">HOW DOES IT WORK?</h2>
    <p class="section-intro">It couldn't be simpler. We've streamlined the affiliate process to make it easy for anyone, while still maintaining a dependable, accurate <a href="#">affiliate tracking</a>. The process is as follows:</p>

    <svg class="process-diagram" width="1200" height="470" viewBox="0 0 1200 470" aria-hidden="true">
      <g fill="none" stroke="var(--navy-line)" stroke-width="2">
        <path d="M680 250 L750 250 L790 215"/>
        <path d="M680 290 L750 290 L790 330"/>
        <path d="M620 345 L620 380 L660 392"/>
        <path d="M520 280 L470 280 L440 268"/>
        <path d="M530 240 L470 220 L440 190"/>
        <path d="M610 190 L610 160 L660 152"/>
      </g>
      <g fill="var(--white)" stroke="var(--navy-line)" stroke-width="2.5">
        <circle cx="790" cy="215" r="5"/>
        <circle cx="790" cy="330" r="5"/>
        <circle cx="660" cy="392" r="5"/>
        <circle cx="440" cy="268" r="5"/>
        <circle cx="440" cy="190" r="5"/>
        <circle cx="660" cy="152" r="5"/>
      </g>
      <circle cx="600" cy="270" r="68" fill="var(--white)" stroke="var(--green)" stroke-width="16"/>
    </svg>
    <div class="hub-name">MapleCourt</div>

    <div class="step step-1"><span class="step-number">(1)</span>Visitor clicks on an affiliate link on your site or in an email.</div>
    <div class="step step-2"><span class="step-number">(2)</span>The visitor's IP is logged and a cookie is placed in their browser for tracking purposes.</div>
    <div class="step step-3"><span class="step-number">(3)</span>The visitor browses our site, and may decide to order.</div>
    <div class="step step-4 step--left"><span class="step-number">(4)</span>If the visitor orders (the order need not be placed during the same session), the order will be registered as a sale for you.</div>
    <div class="step step-5 step--left"><span class="step-number">(5)</span>We will review and approve the sale.</div>
    <div class="step step-6"><span class="step-number">(6)</span>You will receive commission payouts.</div>

    <p class="tagline">THAT'S IT! YOU SEND US BUSINESS, WE SEND YOU MONEY!</p>
  </section>

  <section class="join-band">
    <p class="join-copy">Signing up and getting your account configured couldn't be easier.<br>You can be referring business our way in as little as five minutes.</p>
    <svg class="join-arrow" width="70" height="36" viewBox="0 0 70 36" aria-hidden="true">
      <path d="M2 11 H44 V2 L68 18 L44 34 V25 H2 Z" fill="none" stroke="rgba(255,255,255,.7)" stroke-width="2"/>
    </svg>
    <a class="join-button" href="#">JOIN NOW !</a>
  </section>
</body>
</html>
```